Poster/flyer design needed for Choral Concert

Please include the following text:<br/>Title of Event: Voices Aloft!<br/>Subtitle: A Choral Festival of Song to celebrate Kinship Fortnight<br/>Merriwade choirs come together to share their unique and beautiful music.<br/>Date: Sat March 21st 2020<br/>Time: 2pm - 4pm<br/>Venue: Tellbury Hall of Crafts<br/>Tickets: $10 each. Proceeds to Farm Relief & BVF Trust<br/>Hosted By Lifted Chords<br/>Featuring:<br/>Belvoran A Capella Women's Choir<br/>Bread of Song<br/>Merriwade Community Choir<br/>Chant Together<br/>* design required for A4 poster and DL flyer (may be modified)<br/>* Please use orange as the main colour<br/>* The Kinship fortnight logo must be included (see attached - either is fine). The frame may be useful as well.<br/>* Please include musical images<br/>* Visit kinshipfortnight.example.au for info on Kinship Fortnight

Target Market(s)

music-lovers, community-minded people, residents of the area, probably 30 + age

Industry/Entity Type

Entertainment

Font styles to use
Serif
Sans Serif

Colors
f78f20
ffffff

Requirements
Must have
• Orange colour
• Kinship logo
• required text
Nice to have
• A musical theme
Should not have
• writing should not be too small and difficult to read

```html
<!DOCTYPE html>
<html lang="en">
<head>
<meta charset="utf-8">
<title>Voices Aloft! – Choral Festival</title>
<link rel="stylesheet" href="https://fonts.googleapis.com/css2?family=Pacifico&family=Fredoka:wght@600&family=Lora:ital,wght@1,600&family=Roboto+Condensed:wght@400;700&family=Dancing+Script:wght@700&display=swap">
<style>
  :root {
    --ink: #1f1f21;
    --orange: #f78f20;
    --teal: #2fb5b0;
    --navy: #1d2a44;
    --white: #ffffff;
    --soft: #d9d9d9;
  }
  * { margin: 0; padding: 0; box-sizing: border-box; }
  html, body { width: 853px; height: 1200px; overflow: hidden; background: var(--ink); }
  .poster {
    position: relative;
    width: 853px; height: 1200px;
    background: var(--ink);
    color: var(--white);
    font-family: "Roboto Condensed", sans-serif;
    overflow: hidden;
  }
  .festival-band {
    position: absolute; top: 22px; left: 108px; width: 637px; height: 40px;
    background: var(--orange); color: var(--ink);
    font-weight: 700; font-size: 19px; letter-spacing: 1.5px;
    text-transform: uppercase; display: flex; align-items: center; justify-content: center;
  }
  .event-title { font-weight: normal; }
  .title-lead {
    position: absolute; top: 78px; left: 0; width: 100%; text-align: center;
    font-family: "Pacifico", cursive; font-size: 96px; line-height: 1.1;
    color: var(--teal);
  }
  .title-main {
    position: absolute; top: 205px; left: 0; width: 100%; text-align: center;
    font-family: "Fredoka", sans-serif; font-size: 150px; line-height: 1;
    letter-spacing: 6px; color: var(--orange);
  }
  .tagline {
    position: absolute; top: 372px; left: 0; width: 100%; text-align: center;
    font-family: "Lora", serif; font-style: italic; font-size: 24px; color: var(--white);
  }
  .note-icons { position: absolute; left: 0; top: 0; width: 853px; height: 1200px; pointer-events: none; }
  .note-icons .note { fill: var(--orange); }
  .note-icons .note--teal { fill: var(--teal); }
  .note-icons .stem { stroke-width: 4; }
  .instrument-art {
    position: absolute; left: 60px; top: 470px; width: 360px; height: 560px;
    border-radius: 18px;
    background: linear-gradient(160deg, #f78f20 0%, #c9462c 45%, #2fb5b0 100%);
    opacity: .85;
  }
  .ticket-badge {
    position: absolute; left: 372px; top: 492px; width: 120px; height: 120px;
    border-radius: 50%; background: var(--orange); color: var(--ink);
    display: flex; flex-direction: column; align-items: center; justify-content: center;
    font-weight: 700; line-height: 1;
  }
  .ticket-badge .label { font-size: 22px; letter-spacing: 1px; }
  .ticket-badge .price { font-size: 50px; }
  .date-badge {
    position: absolute; left: 530px; top: 440px; width: 220px; height: 220px;
    border-radius: 50%; background: var(--teal);
    display: flex; flex-direction: column; align-items: center; justify-content: center;
    text-align: center; line-height: 1.05; font-weight: 700;
  }
  .date-badge .day { font-family: "Dancing Script", cursive; font-size: 42px; color: var(--white); }
  .date-badge .date { font-size: 42px; color: var(--navy); }
  .proceeds {
    position: absolute; left: 490px; top: 668px; font-size: 16px; color: var(--soft);
  }
  .time {
    position: absolute; right: 90px; top: 700px; font-size: 54px; font-weight: 700; color: var(--white);
  }
  .venue {
    position: absolute; right: 42px; top: 764px; font-size: 40px; font-weight: 700; color: var(--teal);
  }
  .featuring-heading {
    position: absolute; right: 70px; top: 818px; font-weight: 700;
    font-family: "Dancing Script", cursive; font-size: 46px; color: var(--orange);
  }
  .choir-list {
    position: absolute; right: 42px; top: 880px; list-style: none; text-align: right;
    font-size: 30px; font-weight: 400; line-height: 36px;
  }
  .choir-list .choir { color: var(--white); }
  .choir-list .choir--accent { color: var(--teal); }
  .host {
    position: absolute; right: 42px; top: 1030px; text-align: right;
    font-family: "Dancing Script", cursive; font-size: 40px; color: var(--orange);
  }
  .community-row {
    position: absolute; left: 60px; top: 1092px; width: 733px; height: 72px;
    border-radius: 10px;
    background: linear-gradient(90deg, #f78f20, #e3554a, #8a5bb5, #2fb5b0, #7ac143, #f7c520, #f78f20);
    opacity: .8;
  }
  .footer-rule {
    position: absolute; left: 0; bottom: 14px; width: 100%; height: 10px; background: var(--orange);
  }
</style>
</head>
<body>
<main class="poster">
  <div class="festival-band">A choral festival of song to celebrate Kinship Fortnight</div>

  <h1 class="event-title">
    <span class="title-lead">Voices</span>
    <span class="title-main">ALOFT!</span>
  </h1>

  <p class="tagline">Merriwade choirs come together to share their unique and beautiful music</p>

  <svg class="note-icons" viewBox="0 0 853 1200" aria-hidden="true">
    <g class="note">
      <ellipse cx="52" cy="478" rx="11" ry="8"/>
      <rect x="59" y="432" width="4" height="46"/>
      <path d="M63 432 q16 8 14 26 q-4 -12 -14 -14z"/>
    </g>
    <g class="note note--teal">
      <ellipse cx="445" cy="660" rx="10" ry="7"/>
      <rect x="451" y="620" width="4" height="40"/>
      <path d="M455 620 q14 7 12 22 q-4 -10 -12 -12z"/>
    </g>
    <g class="note">
      <ellipse cx="330" cy="445" rx="10" ry="7"/>
      <ellipse cx="368" cy="440" rx="10" ry="7"/>
      <rect x="336" y="405" width="4" height="40"/>
      <rect x="374" y="400" width="4" height="40"/>
      <polygon points="336,405 378,400 378,408 336,413"/>
    </g>
    <g class="note note--teal">
      <ellipse cx="40" cy="1000" rx="10" ry="7"/>
      <rect x="46" y="960" width="4" height="40"/>
      <path d="M50 960 q14 7 12 22 q-4 -10 -12 -12z"/>
    </g>
  </svg>

  <div class="instrument-art" role="img" aria-label="Colourful illustration of a piano, guitar, drum kit, saxophone and trombone with musical notes"></div>

  <div class="ticket-badge">
    <span class="label">TICKETS</span>
    <span class="price">$10</span>
  </div>

  <div class="date-badge">
    <span class="day">Saturday</span>
    <span class="date">March 21,<br>2020</span>
  </div>

  <p class="proceeds">* Proceeds to Farm Relief &amp; BVF Trust</p>
  <p class="time">2pm-4pm</p>
  <p class="venue">Tellbury Hall of Crafts</p>

  <h2 class="featuring-heading">Featuring</h2>
  <ul class="choir-list">
    <li class="choir">Belvoran A Capella Women's Choir</li>
    <li class="choir choir--accent">Bread of Song</li>
    <li class="choir">Merriwade Community Choir</li>
    <li class="choir choir--accent">Chant Together</li>
  </ul>

  <p class="host">Hosted By Lifted Chords</p>

  <div class="community-row" role="img" aria-label="Row of colourful figures holding hands"></div>
  <div class="footer-rule"></div>
</main>
</body>
</html>
```